Hillcrest BBQ Co. Rub and Sauce Labels

I am bringing to market 3 different meat rubs and 2 BBQ sauces. These rubs and sauces will be sold on an eCommerce website and also at local events. I am looking for simplicity. I believe the BBQ seasoning labels out there are very busy. I am looking for each label to be similar, yet distinct enough to clearly differentiate the different rubs in my offerings. My logo is attached. The Smoky H in my logo is going to be a feature in my brand and would like to have it be a feature on my labels, too. The rubs will be packaged in a traditional clear plastic shaker with a pop-top. I am open to ideas on packaging options as well. The different rubs in the shakers will range in color from very light to dark brown, depending on the ingredients in each rub. Please include all FDA required information on the labels. The rub labels will go on a clear plastic shaker and the sauce will be packaged in a bottle. Thanks for your help and I look forward to seeing your creativity come to life!

Colors

Designer to choose colors to be used in the design.

Requirements
Must have
• Simplicity, yet ability to separate multiple products by simple changes in logo and/or packaging. Please see the attached photo of a competitors bbq sauce - something simple yet flexible.
Nice to have
• Flexibility in design.

```html
<!DOCTYPE html>
<html lang="en">
<head>
<meta charset="utf-8">
<title>Hillcrest BBQ Co. Rub Labels</title>
<link rel="stylesheet" href="https://fonts.googleapis.com/css2?family=Antonio:wght@400;700&display=swap">
<style>
  :root {
    --backdrop: #202020;
    --label-black: #000000;
    --heat-red: #e30f1a;
    --heat-orange: #f08000;
    --sweet-green: #bfdc4a;
    --ink-white: #ffffff;
  }
  html, body {
    margin: 0;
    padding: 0;
    width: 1200px;
    height: 1200px;
    overflow: hidden;
    background: var(--backdrop);
  }
  .canvas {
    position: relative;
    width: 1200px;
    height: 1200px;
    font-family: "Antonio", "Arial Narrow", sans-serif;
  }
  .label {
    position: absolute;
    top: 231px;
    width: 390px;
    height: 721px;
    background: var(--label-black);
  }
  .label--texas { left: 143px; }
  .label--sweet { left: 658px; }

  .label__frame {
    position: absolute;
    left: 0;
    top: 0;
    width: 390px;
    height: 721px;
  }

  .brand {
    position: absolute;
    left: 0;
    right: 0;
    top: 30px;
    text-align: center;
  }
  .brand__dot {
    display: block;
    width: 46px;
    height: 46px;
    margin: 0 auto 12px;
    border-radius: 50%;
  }
  .brand__name {
    margin: 0;
    font-weight: 700;
    font-size: 13px;
    letter-spacing: 0.12em;
    line-height: 1;
  }

  .product-name {
    position: absolute;
    left: 0;
    right: 0;
    margin: 0;
    text-align: center;
    font-weight: 400;
    text-transform: uppercase;
  }
  .product-name span { display: block; }

  .label--texas .product-name {
    top: 196px;
    font-size: 60px;
    line-height: 78px;
    letter-spacing: 0.32em;
    padding-left: 0.32em;
  }
  .label--sweet .product-name {
    top: 188px;
    font-size: 62px;
    line-height: 82px;
    letter-spacing: 0.62em;
    padding-left: 0.62em;
  }

  .shake-badge {
    position: absolute;
    left: 40px;
    top: 507px;
    width: 60px;
    height: 70px;
    border-radius: 50%;
  }

  .tasting-note {
    position: absolute;
    margin: 0;
    text-align: center;
    text-transform: uppercase;
  }
  .label--texas .tasting-note {
    left: 115px;
    width: 185px;
    top: 515px;
    font-size: 11px;
    line-height: 16.6px;
    letter-spacing: 0.55em;
  }
  .label--sweet .tasting-note {
    left: 118px;
    width: 185px;
    top: 520px;
    font-size: 12px;
    line-height: 18.6px;
    letter-spacing: 0.18em;
  }

  .net-volume {
    position: absolute;
    left: 0;
    right: 0;
    top: 608px;
    margin: 0;
    text-align: center;
    font-size: 28px;
    line-height: 36px;
    letter-spacing: 0.22em;
  }
  .origin {
    position: absolute;
    left: 0;
    right: 0;
    top: 655px;
    margin: 0;
    text-align: center;
    font-size: 16px;
    line-height: 20px;
    letter-spacing: 0.2em;
    color: var(--ink-white);
    text-transform: uppercase;
  }

  .ink-heat {
    background: linear-gradient(100deg, var(--heat-red) 20%, var(--heat-orange) 85%);
    -webkit-background-clip: text;
    background-clip: text;
    color: transparent;
  }
  .ink-sweet { color: var(--sweet-green); }

  .label--texas .brand__dot { background: var(--heat-orange); }
  .label--texas .brand__name { color: var(--heat-orange); }
  .label--sweet .brand__dot,
  .label--sweet .brand__name { color: var(--sweet-green); background-color: transparent; }
  .label--sweet .brand__dot { background: var(--sweet-green); }

  .label--texas .shake-badge {
    background: radial-gradient(circle, var(--heat-orange) 0%, var(--heat-red) 45%, rgba(227,15,26,0.15) 75%);
  }
  .label--sweet .shake-badge {
    background: radial-gradient(circle, var(--sweet-green) 0%, rgba(191,220,74,0.6) 45%, rgba(191,220,74,0.12) 75%);
  }
</style>
</head>
<body>
<main class="canvas">

  <section class="label label--texas">
    <svg class="label__frame" viewBox="0 0 390 721" aria-hidden="true">
      <defs>
        <linearGradient id="heat-frame" x1="0" y1="0" x2="0" y2="1">
          <stop offset="0" stop-color="#e30f1a"/>
          <stop offset="1" stop-color="#f08000"/>
        </linearGradient>
      </defs>
      <rect x="11.5" y="12.5" width="365" height="696" rx="23" fill="none" stroke="url(#heat-frame)" stroke-width="5"/>
    </svg>
    <div class="brand">
      <span class="brand__dot"></span>
      <p class="brand__name">HILLCREST BBQ CO.</p>
    </div>
    <h2 class="product-name ink-heat">
      <span>Texas</span><span>Style</span><span>Meat</span><span>Rub</span>
    </h2>
    <div class="shake-badge" role="img" aria-label="Shake well badge with hand-lettered words around a small flame"></div>
    <p class="tasting-note ink-heat">The sweet brown sugar mingled with the spicy chili powder gives the best of both worlds</p>
    <p class="net-volume ink-heat">750 ML</p>
    <p class="origin">Made in Sample State</p>
  </section>

  <section class="label label--sweet">
    <svg class="label__frame" viewBox="0 0 390 721" aria-hidden="true">
      <rect x="13.5" y="12.5" width="365" height="696" rx="23" fill="none" stroke="#bfdc4a" stroke-width="5"/>
    </svg>
    <div class="brand">
      <span class="brand__dot"></span>
      <p class="brand__name">HILLCREST BBQ CO.</p>
    </div>
    <h2 class="product-name ink-sweet">
      <span>Sweet</span><span>BBQ</span><span>Meat</span><span>Rub</span>
    </h2>
    <div class="shake-badge" role="img" aria-label="Shake well badge with hand-lettered words around a small flame"></div>
    <p class="tasting-note ink-sweet">Well rounded seasoning, with sweetness as the most primary note on the palate</p>
    <p class="net-volume ink-sweet">750 ML</p>
    <p class="origin">Made in Sample State</p>
  </section>

</main>
</body>
</html>
```